"Thank You" flyer design

We need a "thank you" flyer that will be sent out with all our products.
a6 size landscape,
We manufacture personalised shaped signs.
I've attached a rough idea of what we are after, but would like it to be improved upon with some artistic flare..

Side one - We would like the flyer to have a simple message - "thank you for shopping with us"

Side two - we would also like our logo and a union jack made in the UK badge and our address and contact details with our website www.pelminsignworks.co.uk being the most prominent..

We are after a simple bold design what would be printed on a small a6 card that people might hopefully want to keep, so the end design needs to be pretty cool.

Industry/Entity Type

Shopping

Font styles to use
Serif
Sans Serif

```html
<!DOCTYPE html>
<html lang="en">
<head>
<meta charset="utf-8">
<title>Thank You Flyer</title>
<link rel="stylesheet" href="https://fonts.googleapis.com/css2?family=Open+Sans:wght@800&family=Fira+Sans+Extra+Condensed:wght@700&family=Arimo:wght@400&display=swap">
<style>
  :root {
    --brand-blue: #0b6fb8;
    --brand-red: #e42c37;
    --paper: #ffffff;
  }
  * { margin: 0; padding: 0; box-sizing: border-box; }
  html, body { width: 1200px; height: 848px; overflow: hidden; background: var(--paper); }
  .flyer {
    position: relative;
    width: 1200px;
    height: 848px;
    background: var(--paper);
  }
  .header-band {
    position: absolute;
    left: 0; top: 0;
    width: 1200px; height: 208px;
    background: var(--brand-blue);
    display: flex; align-items: center; justify-content: center;
  }
  .headline {
    font-family: "Open Sans", sans-serif;
    font-weight: 800;
    font-size: 172px;
    line-height: 1;
    color: var(--paper);
    letter-spacing: 2px;
    margin-top: -12px;
  }
  .tagline {
    position: absolute;
    left: 0; top: 318px;
    width: 1200px;
    text-align: center;
    font-family: "Fira Sans Extra Condensed", sans-serif;
    font-weight: 700;
    font-size: 106px;
    line-height: 1;
    letter-spacing: 11px;
    color: var(--brand-red);
  }
  .divider {
    position: absolute;
    left: 108px; top: 514px;
    width: 976px; height: 110px;
  }
  .web-address {
    position: absolute;
    left: 0; top: 650px;
    width: 1200px;
    display: flex; align-items: center; justify-content: center;
    gap: 22px;
  }
  .web-icon { width: 104px; height: 108px; flex: none; }
  .web-url {
    font-family: "Arimo", sans-serif;
    font-weight: 400;
    font-size: 96px;
    line-height: 1;
    color: var(--brand-red);
    letter-spacing: -1px;
  }
</style>
</head>
<body>
<main class="flyer">
  <header class="header-band">
    <h1 class="headline">THANK YOU</h1>
  </header>

  <p class="tagline">FOR SHOPPING WITH US</p>

  <svg class="divider" viewBox="0 0 976 110" aria-hidden="true">
    <line x1="0" y1="57" x2="976" y2="57" stroke="var(--brand-blue)" stroke-width="2"/>
    <circle cx="488" cy="52" r="52" fill="var(--paper)" stroke="var(--brand-blue)" stroke-width="2"/>
    <g fill="none" stroke="var(--brand-red)" stroke-width="5" stroke-linejoin="round" stroke-linecap="round">
      <path d="M433 12 H446 L452 62 H520"/>
      <path d="M446 22 H524 L518 50 H451"/>
      <line x1="462" y1="22" x2="463" y2="50"/>
      <line x1="478" y1="22" x2="479" y2="50"/>
      <line x1="494" y1="22" x2="494" y2="50"/>
      <line x1="510" y1="22" x2="508" y2="50"/>
    </g>
    <circle cx="462" cy="80" r="7" fill="var(--brand-red)"/>
    <circle cx="512" cy="80" r="7" fill="var(--brand-red)"/>
  </svg>

  <div class="web-address">
    <svg class="web-icon" viewBox="0 0 104 108" aria-hidden="true">
      <g fill="none" stroke="var(--brand-blue)" stroke-width="9">
        <path d="M92 62 A44 44 0 1 0 62 92"/>
        <path d="M50 6 C28 30 28 74 50 96"/>
        <path d="M50 6 C66 24 70 42 70 54"/>
        <line x1="8" y1="36" x2="92" y2="36"/>
        <line x1="8" y1="64" x2="56" y2="64"/>
        <line x1="50" y1="6" x2="50" y2="96"/>
      </g>
      <path d="M62 56 L100 78 L84 82 L96 100 L88 105 L76 87 L66 97 Z" fill="var(--brand-blue)"/>
    </svg>
    <span class="web-url">pelminsignworks.co.uk</span>
  </div>
</main>
</body>
</html>
```